Stockly Z5 - DL Flyer

Flyer designed with the following points:

Retail Point of Sale
Hardware and Software
Highly customisable to suit your business
Free POS appraisal and Quotes
E-commerce Integrations with your existing website
Multiple Store Capability
One on one set up and support
100% Tax Deductable
From only $9.95 per week

1300 462 718
admin@stocklyz5.com.au
www.stocklyz5.com.au

```html
<!DOCTYPE html>
<html lang="en">
<head>
<meta charset="utf-8">
<title>Stockly Z5 – DL Flyer</title>
<link rel="stylesheet" href="https://fonts.googleapis.com/css2?family=Montserrat:wght@300;400;500;600;700;800&display=swap">
<style>
  :root{
    --blue:#29a8e0;
    --ink:#2f2f31;
    --ink-soft:#4d4d50;
    --card:#f1f1f2;
    --paper:#ffffff;
    --backdrop:#c9c9ca;
  }
  *{box-sizing:border-box;margin:0;padding:0}
  html,body{width:750px;height:1200px;overflow:hidden;background:var(--backdrop)}
  body{font-family:"Montserrat",Arial,sans-serif;color:var(--ink);position:relative}

  .flyer{position:absolute;top:229px;width:513px;height:1090px;background:var(--paper);overflow:hidden;
    transform:scale(.68);transform-origin:top left;box-shadow:0 8px 24px rgba(0,0,0,.25)}
  .flyer--front{left:18px}
  .flyer--back{left:383px;background:linear-gradient(180deg,#fff 0%,#fff 55%,#ececec 80%,#f4f4f4 100%)}

  .abs{position:absolute}
  .header-shape{position:absolute;left:0;top:0;width:513px;height:200px}
  .brand{position:absolute;top:40px;left:0;width:100%;text-align:center;color:#fff;
    font-weight:800;font-size:50px;letter-spacing:1px;line-height:1}

  /* tax badges */
  .badge{position:absolute;text-align:center;line-height:1}
  .badge svg{position:absolute;left:0;top:0}
  .badge__text{position:absolute;left:0;top:0;width:100%;height:100%;display:flex;flex-direction:column;
    align-items:center;justify-content:center;font-weight:800}
  .badge--front{left:38px;top:193px;width:144px;height:144px;transform:rotate(-16deg)}
  .badge--front .pct{color:#fff;font-size:32px}
  .badge--front .tax{color:var(--blue);font-size:46px;margin-top:-4px}
  .badge--front .ded{color:#fff;font-size:13px;margin-top:0}
  .badge--back{left:178px;top:850px;width:160px;height:160px}
  .badge--back .pct{color:#fff;font-size:36px}
  .badge--back .tax{color:var(--ink);font-size:50px;margin-top:-4px}
  .badge--back .ded{color:#fff;font-size:14px;margin-top:2px}

  .devices{position:absolute;left:0;top:230px;width:513px;height:380px}

  .headline{position:absolute;left:45px;width:425px;font-weight:800;line-height:1;white-space:nowrap}
  .headline--blue{top:652px;color:var(--blue);font-size:58px}
  .headline--dark{top:712px;color:var(--ink);font-size:64px}
  .headline--thin{top:776px;color:var(--blue);font-size:29px;font-weight:300;letter-spacing:13.2px}

  .features{position:absolute;top:826px;list-style:none;font-size:14px;font-weight:600;line-height:17px}
  .features li{position:relative;padding-left:18px;margin-bottom:10px}
  .features--left{left:45px;width:210px}
  .features--right{left:267px;width:220px}
  .tick{position:absolute;left:0;top:2px;width:12px;height:12px;border:1.6px solid var(--blue);border-radius:2px}
  .tick::after{content:"";position:absolute;left:3px;top:-2px;width:4px;height:8px;border:solid var(--blue);
    border-width:0 2px 2px 0;transform:rotate(40deg)}

  .offer{position:absolute;left:93px;top:958px;width:325px;height:54px;border-radius:27px;background:var(--blue);
    display:flex;align-items:center;justify-content:center;gap:10px}
  .offer__lead{color:var(--ink);font-size:18px;font-weight:500}
  .offer__price{color:#fff;font-size:42px;font-weight:800;line-height:1}
  .offer__price sup{font-size:22px;vertical-align:16px}
  .offer__unit{color:var(--ink);font-size:17px;font-weight:800;line-height:.95}

  .footer-shape{position:absolute;left:0;bottom:0;width:513px;height:80px}
  .contact{position:absolute;left:0;top:1032px;width:100%;display:flex;align-items:center;justify-content:center;gap:22px;color:#fff}
  .contact__phone{display:flex;align-items:center;gap:3px;font-size:26px;font-weight:600}
  .contact__lines{font-size:13px;font-weight:500;line-height:15px}
  .contact__lines span{display:flex;align-items:center;gap:5px}

  /* price list */
  .title-pill{position:absolute;left:93px;top:135px;width:325px;height:54px;border-radius:27px;background:var(--ink);
    color:#fff;font-weight:700;font-size:34px;letter-spacing:2px;text-align:center;line-height:54px}
  .plan{position:absolute;left:40px;width:435px;height:150px}
  .plan__card{position:absolute;left:0;top:0;width:280px;height:92px;border-radius:10px 0 0 10px;
    background:linear-gradient(90deg,var(--card),#fafafa);box-shadow:0 5px 6px rgba(0,0,0,.12)}
  .plan__name{position:absolute;left:26px;top:24px;color:var(--blue);font-size:25px;font-weight:800;line-height:1;white-space:nowrap}
  .plan__sub{position:absolute;left:26px;top:51px;font-size:15px;font-weight:500}
  .plan__price{position:absolute;left:258px;top:0;width:177px;height:92px;border-radius:10px;background:var(--ink);
    color:#fff;font-size:40px;font-weight:700;display:flex;align-items:center;justify-content:center;
    box-shadow:0 5px 6px rgba(0,0,0,.2)}
  .plan__price--soft{background:var(--ink-soft)}
  .plan__price sup{font-size:20px;vertical-align:14px}
  .plan__specs{position:absolute;left:12px;top:110px;display:flex;gap:18px;font-size:14px;font-weight:600;white-space:nowrap}
  .plan__specs span{position:relative;padding-left:16px}
</style>
</head>
<body>

<!-- FRONT -->
<section class="flyer flyer--front">
  <svg class="header-shape" viewBox="0 0 513 200" aria-hidden="true">
    <path fill="var(--blue)" d="M0,0H513V128C440,118 380,120 340,160 C300,110 200,90 130,125 C105,138 92,150 85,168 V128 H0Z"/>
  </svg>
  <div class="brand">STOCKLY Z5</div>

  <svg class="devices" viewBox="0 0 513 380" role="img" aria-label="Laptop, tablet and phone showing the point of sale software screens">
    <defs>
      <linearGradient id="screenFill" x1="0" y1="0" x2="0" y2="1">
        <stop offset="0" stop-color="#e9eef2"/><stop offset="1" stop-color="#cfd6dc"/>
      </linearGradient>
    </defs>
    <circle cx="400" cy="70" r="55" fill="var(--blue)"/>
    <path fill="var(--blue)" d="M20,310 C120,390 390,390 490,310 Z"/>
    <rect x="70" y="45" width="390" height="280" rx="10" fill="url(#screenFill)"/>
  </svg>

  <div class="badge badge--front">
    <svg width="144" height="144" viewBox="0 0 144 144" aria-hidden="true">
      <circle cx="72" cy="72" r="66" fill="var(--ink)"/>
      <circle cx="72" cy="72" r="67" fill="none" stroke="var(--ink)" stroke-width="8" stroke-dasharray="5 4"/>
    </svg>
    <div class="badge__text"><span class="pct">100%</span><span class="tax">TAX</span><span class="ded">DEDUCTABLE</span></div>
  </div>

  <h1 class="headline headline--blue">AUSTRALIAS</h1>
  <div class="headline headline--dark">FAVOURITE</div>
  <div class="headline headline--thin">POST SOFTWARE</div>

  <ul class="features features--left">
    <li><i class="tick"></i>Hardware and Software</li>
    <li><i class="tick"></i>Highly customisable to suit your business</li>
    <li><i class="tick"></i>Free POS appraisal and Quotes</li>
  </ul>
  <ul class="features features--right">
    <li><i class="tick"></i>E-commerce Integrations with your existing website</li>
    <li><i class="tick"></i>Multiple Store Capability</li>
    <li><i class="tick"></i>One on one set up and support</li>
  </ul>

  <div class="offer">
    <span class="offer__lead">From only</span>
    <span class="offer__price"><sup>$</sup>9.95</span>
    <span class="offer__unit">PER<br>WEEK</span>
  </div>

  <svg class="footer-shape" viewBox="0 0 513 80" aria-hidden="true">
    <path fill="var(--ink)" d="M0,80V50 C120,0 393,0 513,50 V80Z"/>
  </svg>
  <div class="contact">
    <span class="contact__phone">
      <svg width="20" height="20" viewBox="0 0 24 24" aria-hidden="true"><path fill="var(--blue)" d="M6.6 10.8a15 15 0 0 0 6.6 6.6l2.2-2.2c.3-.3.7-.4 1-.2 1.1.4 2.3.6 3.6.6.6 0 1 .4 1 1V20c0 .6-.4 1-1 1A17 17 0 0 1 3 4c0-.6.4-1 1-1h3.5c.6 0 1 .4 1 1 0 1.3.2 2.5.6 3.6.1.3 0 .7-.2 1z"/></svg>
      1300 462 718
    </span>
    <span class="contact__lines">
      <span><svg width="8" height="7" viewBox="0 0 8 7" aria-hidden="true"><rect width="8" height="7" fill="var(--blue)"/></svg>admin@stocklyz5.com.au</span>
      <span><svg width="8" height="8" viewBox="0 0 8 8" aria-hidden="true"><circle cx="4" cy="4" r="4" fill="var(--blue)"/></svg>www.stocklyz5.com.au</span>
    </span>
  </div>
</section>

<!-- BACK -->
<section class="flyer flyer--back">
  <svg class="header-shape" viewBox="0 0 513 200" aria-hidden="true">
    <path fill="var(--blue)" d="M0,0H513V70 C470,140 380,168 256,168 C132,168 40,140 0,70Z"/>
  </svg>
  <div class="brand">STOCKLY Z5</div>
  <h2 class="title-pill">PRICE LIST</h2>

  <div class="plan" style="top:229px">
    <div class="plan__card"><div class="plan__name">SMALL RETAIL</div><div class="plan__sub">Software Package</div></div>
    <div class="plan__price"><sup>$</sup>9.95</div>
    <div class="plan__specs"><span><i class="tick"></i>1-2 Staff Users</span><span><i class="tick"></i>1 Cash Register</span><span><i class="tick"></i>1 Store Location</span></div>
  </div>
  <div class="plan" style="top:388px">
    <div class="plan__card"><div class="plan__name">MEDIUM RETAIL</div><div class="plan__sub">Software Package</div></div>
    <div class="plan__price plan__price--soft"><sup>$</sup>17.95</div>
    <div class="plan__specs"><span><i class="tick"></i>1-2 Staff Users</span><span><i class="tick"></i>1 Cash Register</span><span><i class="tick"></i>1 Store Location</span></div>
  </div>
  <div class="plan" style="top:546px">
    <div class="plan__card"><div class="plan__name">LARGE RETAIL</div><div class="plan__sub">Software Package</div></div>
    <div class="plan__price"><sup>$</sup>34.95</div>
    <div class="plan__specs"><span><i class="tick"></i>1-2 Staff Users</span><span><i class="tick"></i>1 Cash Register</span><span><i class="tick"></i>1 Store Location</span></div>
  </div>
  <div class="plan" style="top:705px">
    <div class="plan__card"><div class="plan__name">ENTERPRISE</div><div class="plan__sub">Software Package</div></div>
    <div class="plan__price plan__price--soft"><sup>$</sup>49.95</div>
    <div class="plan__specs"><span><i class="tick"></i>1-2 Staff Users</span><span><i class="tick"></i>1 Cash Register</span><span><i class="tick"></i>1 Store Location</span></div>
  </div>

  <svg class="footer-shape" viewBox="0 0 513 80" aria-hidden="true">
    <path fill="var(--ink)" d="M0,80V50 C120,0 393,0 513,50 V80Z"/>
  </svg>

  <div class="badge badge--back">
    <svg width="160" height="160" viewBox="0 0 160 160" aria-hidden="true">
      <circle cx="80" cy="80" r="74" fill="var(--blue)"/>
      <circle cx="80" cy="80" r="75" fill="none" stroke="var(--blue)" stroke-width="8" stroke-dasharray="5 4"/>
      <circle cx="80" cy="80" r="67" fill="none" stroke="#fff" stroke-width="1.5"/>
    </svg>
    <div class="badge__text"><span class="pct">100%</span><span class="tax">TAX</span><span class="ded">DEDUCTABLE</span></div>
  </div>

  <div class="contact">
    <span class="contact__phone">
      <svg width="20" height="20" viewBox="0 0 24 24" aria-hidden="true"><path fill="var(--blue)" d="M6.6 10.8a15 15 0 0 0 6.6 6.6l2.2-2.2c.3-.3.7-.4 1-.2 1.1.4 2.3.6 3.6.6.6 0 1 .4 1 1V20c0 .6-.4 1-1 1A17 17 0 0 1 3 4c0-.6.4-1 1-1h3.5c.6 0 1 .4 1 1 0 1.3.2 2.5.6 3.6.1.3 0 .7-.2 1z"/></svg>
      1300 462 718
    </span>
    <span class="contact__lines">
      <span><svg width="8" height="7" viewBox="0 0 8 7" aria-hidden="true"><rect width="8" height="7" fill="var(--blue)"/></svg>admin@stocklyz5.com.au</span>
      <span><svg width="8" height="8" viewBox="0 0 8 8" aria-hidden="true"><circle cx="4" cy="4" r="4" fill="var(--blue)"/></svg>www.stocklyz5.com.au</span>
    </span>
  </div>
</section>

</body>
</html>
```